Business Card Design

We would like a colorful, engaging, welcoming business card, utilizing our picture of a local lighthouse. We are a Church. We would like the design to mostly feature the colour blue.
Thank you so much to all Designers who sent in submissions to us - it was really hard to make a decision, they were all of such high quality. We would not hesitate to recommend Sketch Harbor to other churches/ businesses.
Kestrel Beacon Fellowship
Industry/Entity Type
Business
Contact Information for Business Card
Kestrel Beacon Fellowship Inc, 17 Merrow Rd, TALLOWVALE WA 6412, Ph: (08) 9517 4063, E: beaconfellowship@quorvex.example, Facebook logo - Kestrel Beacon Fellowship Inc, Sunday Service 10am, "For God sent not his Son into the world to condemn the world; but that the world through Him might be saved." John 3:17.

```html
<!DOCTYPE html>
<html lang="en">
<head>
<meta charset="utf-8">
<title>Kestrel Beacon Fellowship Inc — Business Card</title>
<link rel="stylesheet" href="https://fonts.googleapis.com/css2?family=Open+Sans:wght@700&display=swap">
<style>
  :root {
    --page-bg: #e6e8ea;
    --card-blue: #00a7ea;
    --sky-deep: #3d4a86;
    --sky-mid: #5a6aa8;
    --sky-glow: #b9c6ec;
    --headland: #2b3150;
    --title-cyan: #17b3ea;
    --ink-white: #ffffff;
  }
  html, body {
    margin: 0;
    width: 1200px;
    height: 898px;
    overflow: hidden;
    background: var(--page-bg);
  }
  .stage {
    width: 1200px;
    height: 898px;
    display: flex;
    align-items: center;
    justify-content: center;
  }
  .business-card {
    position: relative;
    width: 900px;
    height: 514px;
    background: var(--card-blue);
    overflow: hidden;
    font-family: "Open Sans", Arial, sans-serif;
    font-weight: 700;
    color: var(--ink-white);
    box-shadow: 0 6px 18px rgba(0, 0, 0, 0.18);
  }
  .lighthouse-photo {
    position: absolute;
    left: 0;
    top: 0;
    width: 900px;
    height: 215px;
    background:
      radial-gradient(ellipse 160px 110px at 330px 150px, var(--sky-glow) 0%, rgba(185, 198, 236, 0.35) 45%, rgba(185, 198, 236, 0) 100%),
      linear-gradient(180deg, var(--sky-deep) 0%, var(--sky-mid) 70%, var(--headland) 100%);
  }
  .ministry-name {
    position: absolute;
    left: 220px;
    top: 52px;
    margin: 0;
    font-size: 27px;
    letter-spacing: 0.2px;
    color: var(--title-cyan);
    white-space: nowrap;
  }
  .divider {
    position: absolute;
    left: 468px;
    top: 248px;
    width: 0;
    height: 140px;
    border-left: 5px solid var(--ink-white);
    transform: rotate(-12deg);
    transform-origin: top left;
  }
  .address {
    position: absolute;
    right: 40px;
    top: 234px;
    margin: 0;
    text-align: right;
    font-style: normal;
    font-size: 19px;
    line-height: 1.3;
  }
  .contact {
    position: absolute;
    left: 40px;
    bottom: 56px;
    margin: 0;
    font-size: 21px;
    line-height: 1.35;
  }
  .contact p { margin: 0; }
</style>
</head>
<body>
  <main class="stage">
    <article class="business-card">
      <div class="lighthouse-photo" role="img" aria-label="Photograph of a local lighthouse on a headland at dusk, its beam glowing against a purple-blue sky"></div>
      <h1 class="ministry-name">Kestrel Beacon Fellowship Inc</h1>
      <div class="divider" aria-hidden="true"></div>
      <address class="address">
        Address:<br>
        Kestrel Beacon<br>
        Fellowship Inc, 17<br>
        Merrow Rd, TALLOWVALE
      </address>
      <div class="contact">
        <p class="contact-phone">Ph: (08) 9517 4063</p>
        <p class="contact-email">Email: beaconfellowship@quorvex.example</p>
      </div>
    </article>
  </main>
</body>
</html>
```